RTB CONTRACTING

I am looking for a logo/design for my business. Would like some unique symbol, would also like it to be double sided. On the back perhaps 3 pictures of some work we have done. I will attach some photos.

I would also like the colours to be orange and black or a dark grey and Orange.

Only writing I would like to see are:

(Contact number) 416-382-7164
(Name) Derek Holloway
(Email) dholloway@mailbox-example.ca

```html
<!DOCTYPE html>
<html lang="en">
<head>
<meta charset="utf-8">
<title>RTB Contracting – Business Card</title>
<link rel="stylesheet" href="https://fonts.googleapis.com/css2?family=Quicksand:wght@500;600;700&display=swap">
<style>
  :root {
    --charcoal: #3e3e3e;
    --light-grey: #e6e6e6;
    --orange: #ef6c22;
    --white: #ffffff;
    --page: #ffffff;
  }
  * { box-sizing: border-box; margin: 0; padding: 0; }
  html, body {
    width: 1200px; height: 1000px; overflow: hidden;
    background: var(--page);
    font-family: "Quicksand", sans-serif;
  }
  .canvas { position: relative; width: 1200px; height: 1000px; }

  .card { position: absolute; background: var(--charcoal); overflow: hidden; }

  /* Front */
  .card-front { left: 275px; top: 73px; width: 700px; height: 411px; }
  .front-brand {
    position: absolute; left: 0; top: 0; width: 100%; height: 328px;
    display: flex; align-items: center; justify-content: center;
    color: var(--orange); font-weight: 700; font-size: 50px; letter-spacing: 3px;
  }
  .front-divider {
    position: absolute; left: 0; top: 328px; width: 100%; height: 9px;
    background: var(--light-grey);
  }
  .front-email {
    position: absolute; left: 0; top: 337px; width: 100%; height: 74px;
    display: flex; align-items: center; justify-content: center;
    color: var(--white); font-size: 22px; font-weight: 600;
  }

  /* Back */
  .card-back { left: 276px; top: 528px; width: 700px; height: 410px; }
  .gallery-rule { position: absolute; left: 0; width: 100%; height: 8px; background: var(--light-grey); }
  .gallery-rule.top { top: 64px; }
  .gallery-rule.bottom { top: 224px; }
  .gallery { position: absolute; left: 0; top: 72px; width: 100%; height: 152px; display: flex; gap: 2px; }
  .work-photo { height: 100%; }
  .work-photo.basement { width: 228px; background: linear-gradient(160deg, #efe9df, #c9b9a0); }
  .work-photo.kitchen { width: 232px; background: linear-gradient(160deg, #b7a58c, #5b3d2a); }
  .work-photo.living { flex: 1; background: linear-gradient(160deg, #f4f3f0, #cdb48e); }

  .name-bar { position: absolute; left: 0; top: 285px; width: 134px; height: 28px; background: var(--light-grey); }
  .contact-name {
    position: absolute; left: 142px; top: 283px;
    color: var(--white); font-size: 20px; font-weight: 600;
  }
  .contact-list { position: absolute; left: 16px; top: 333px; list-style: none; }
  .contact-list li {
    display: flex; align-items: center; gap: 4px; height: 17.5px;
    color: var(--white); font-size: 12.5px; font-weight: 600;
  }
  .contact-list svg { width: 13px; height: 13px; flex: none; }

  .back-brand {
    position: absolute; right: 40px; top: 300px;
    color: var(--orange); font-weight: 700; font-size: 28px; letter-spacing: 2px;
  }
</style>
</head>
<body>
<main class="canvas">

  <section class="card card-front" aria-label="Card front">
    <div class="front-brand">RTB CONTRACTING</div>
    <div class="front-divider"></div>
    <div class="front-email">dholloway@mailbox-example.ca</div>
  </section>

  <section class="card card-back" aria-label="Card back">
    <div class="gallery-rule top"></div>
    <div class="gallery">
      <div class="work-photo basement" role="img" aria-label="Photo of a finished basement play area"></div>
      <div class="work-photo kitchen" role="img" aria-label="Photo of a renovated kitchen with wood cabinets"></div>
      <div class="work-photo living" role="img" aria-label="Photo of a bright renovated living room"></div>
    </div>
    <div class="gallery-rule bottom"></div>

    <div class="name-bar"></div>
    <div class="contact-name">Derek Holloway</div>

    <ul class="contact-list">
      <li>
        <svg viewBox="0 0 13 13" aria-hidden="true"><rect x="0.5" y="0.5" width="12" height="12" rx="2" fill="none" stroke="#fff"/><path d="M4 3.2l1.3 1.6-.8.9c.5 1.1 1.3 1.9 2.4 2.4l.9-.8 1.6 1.3-.8 1.2C6 9.6 3.4 7 3.2 4z" fill="#fff"/></svg>
        416-382-7164
      </li>
      <li>
        <svg viewBox="0 0 13 13" aria-hidden="true"><rect x="0.5" y="0.5" width="12" height="12" rx="2" fill="none" stroke="#fff"/><rect x="3" y="4" width="7" height="5" fill="#fff"/></svg>
        RTBContracting
      </li>
      <li>
        <svg viewBox="0 0 13 13" aria-hidden="true"><rect x="0.5" y="0.5" width="12" height="12" rx="2" fill="none" stroke="#fff"/><circle cx="6.5" cy="6.5" r="3.8" fill="none" stroke="#fff"/><path d="M2.7 6.5h7.6M6.5 2.7v7.6" stroke="#fff" stroke-width="0.8"/></svg>
        dholloway@mailbox-example.ca
      </li>
    </ul>

    <div class="back-brand">RTB CONTRACTING</div>
  </section>

</main>
</body>
</html>
```